Graphics for website image slider

We need 4 banners for website:

We provide software development services to very small to large Businesses. The focus of these 4 banners is to portray the four steps approach to our consulting process: Assess, Analyse, Plan and Deploy

Currently we have the following on our website:
http://www.lumertix.com

We are redesigning the website and want to use 4 sliding graphics to portray the same thing, and the new site is being designed here:
http://www.lumertixonline.com/lumertix

You can use stock photos for each banner or your own creativity.

The images should be 1140px wide and about 420px High.

You can use any modern font such as google font. Not just curly fonts!

Reason: Not yet able to select the final design.

I have updated the colors and how they are supposed to flow because I noticed that some designs did not follow that (We are consultants and really want to understand our process in a powerful way):

ASSESS: Orange color (1st or 5th color above)

ANALYSE: Yellow (2nd or 6th color above)

PLAN: Green (3rd or 7th color above)

DEPLOY: Blue (4th or 8th color above)

=================================================

Some designers also made mistakes in typing the text (Please copy and paste from below):

ASSESS

We gather information and data

to identify and delineate

your central and most pressing business and IT issues.

ANALYSE

We show you exactly where you are in terms of IT maturity

using our optimization tools.

We then build an IT roadmap to help you get to the next level.

PLAN:

We identify the IT products and processes necessary to implement the solution.

We then create a detailed plan of action and technical specifications.

DEPLOY

Finally, we utilize industry best practices and repeatable development and

deployment methods to ensure efficiency and high quality results

that satisfy and bring improvement within budget and timeline.

                                   

Target Market(s)

http://www.lumertix.com

Industry/Entity Type

Software

Font styles to use
Sans Serif
Other font styles liked:
• Any other modern font (No curly fonts)

Colors
fee18a
fbf289
cadf82
86cae6
f78f20
ffc214
9aca3c
0692cd

Requirements
Must have
• Graphic should convey the message for each process

```html
<!DOCTYPE html>
<html lang="en">
<head>
<meta charset="utf-8">
<title>Lumertix — Home</title>
<link href="https://fonts.googleapis.com/css2?family=Open+Sans:wght@300;400;600;700&family=Shadows+Into+Light&display=swap" rel="stylesheet">
<style>
  :root {
    --brand: #8b0a1c;
    --brand-line: #8e1320;
    --page-bg: #ececec;
    --panel: #ffffff;
    --topbar: #f4f4f4;
    --header: #f9f9f9;
    --ink: #222222;
    --nav-ink: #333333;
    --muted: #777777;
    --slider-bg: #1b2327;
    --circle-fill: #e0e0e0;
    --dash: #8a8a8a;
    --assess: #f78f20;
    --assess-soft: #fee18a;
    --analyse: #ffc214;
    --plan: #9aca3c;
    --deploy: #0692cd;
  }
  * { box-sizing: border-box; margin: 0; padding: 0; }
  html, body { width: 1155px; height: 1200px; overflow: hidden; }
  body {
    background: var(--page-bg);
    font-family: "Open Sans", Arial, sans-serif;
    position: relative;
  }
  .site {
    position: absolute; left: 36px; top: 22px; width: 1082px; height: 1178px;
    background: var(--panel);
    border-top: 4px solid var(--brand-line);
    box-shadow: 0 0 6px rgba(0,0,0,.08);
    overflow: hidden;
  }
  .topbar { position: absolute; left: 0; top: 0; width: 100%; height: 70px; background: var(--topbar); }
  .social { position: absolute; left: 27px; top: 23px; display: flex; gap: 4px; }
  .social-dot, .tool-dot {
    width: 27px; height: 27px; border-radius: 50%;
    background: #fff; box-shadow: 0 1px 2px rgba(0,0,0,.25);
  }
  .social .social-dot:nth-child(3) { margin-left: 2px; }
  .tools { position: absolute; left: 690px; top: 25px; display: flex; gap: 8px; align-items: center; }
  .pause { display: flex; gap: 3px; justify-content: center; align-items: center; }
  .pause span { width: 5px; height: 10px; background: #c8c8c8; }
  .flag { display: flex; justify-content: center; align-items: center; }
  .flag span { width: 14px; height: 10px; background: linear-gradient(#b22234 0 20%, #fff 20% 40%, #b22234 40% 60%, #fff 60% 80%, #b22234 80%); position: relative; }
  .flag span::before { content: ""; position: absolute; left: 0; top: 0; width: 6px; height: 5px; background: #3c3b6e; }
  .account { position: absolute; top: 36px; left: 777px; display: flex; gap: 27px; font-size: 10.5px; color: var(--brand); text-transform: uppercase; }
  .search {
    position: absolute; left: 906px; top: 28px; width: 152px; height: 30px;
    border: 1px solid #ddd; border-radius: 16px; background: #fff;
    font-size: 11px; color: #999; padding: 7px 12px;
  }
  .search svg { position: absolute; right: 12px; top: 8px; }

  .header { position: absolute; left: 0; top: 70px; width: 100%; height: 110px; background: var(--header); }
  .brand { position: absolute; left: 30px; top: 28px; display: flex; align-items: center; gap: 10px; }
  .brand-mark { width: 30px; height: 30px; background: var(--brand); }
  .brand-name { font-size: 30px; font-weight: 700; color: var(--brand); letter-spacing: 1px; }
  .nav { position: absolute; top: 72px; left: 458px; font-size: 11px; font-weight: 700; color: var(--nav-ink); text-transform: uppercase; }
  .nav a { color: inherit; text-decoration: none; position: absolute; white-space: nowrap; }
  .nav a.active { color: var(--brand); }
  .nav .caret { font-size: 8px; margin-left: 2px; }

  .slider {
    position: absolute; left: 27px; top: 197px; width: 1029px; height: 378px;
    background: var(--slider-bg); border-radius: 5px; overflow: hidden;
  }
  .slider-photo {
    position: absolute; left: 463px; top: 0; width: 566px; height: 100%;
    background: linear-gradient(100deg, #1b2327 0%, #3a3128 35%, #a65a18 70%, #f7a54a 100%);
  }
  .slide-step { position: absolute; left: 53px; top: 64px; font-size: 11px; font-weight: 700; letter-spacing: 2px; color: var(--assess); text-transform: uppercase; }
  .slide-title { position: absolute; left: 51px; top: 78px; font-size: 48px; font-weight: 300; color: #fff; line-height: 60px; }
  .slide-title::after { content: ""; display: block; width: 56px; height: 3px; background: var(--assess); margin-top: 2px; }
  .slide-text { position: absolute; left: 53px; top: 150px; width: 360px; font-size: 12px; line-height: 20px; color: #9aa4a8; }
  .slide-btn {
    position: absolute; left: 53px; top: 221px; width: 78px; height: 27px;
    background: #fff; border-radius: 3px; color: var(--brand); font-size: 12px;
    display: flex; align-items: center; justify-content: center;
  }
  .slide-pager {
    position: absolute; left: 21px; top: 340px; width: 86px; height: 20px; border-radius: 10px;
    background: #11181b; display: flex; align-items: center; gap: 9px; padding-left: 11px;
  }
  .slide-pager span { width: 9px; height: 9px; border-radius: 50%; }
  .slide-pager .assess { border: 2px solid var(--assess); }
  .slide-pager .analyse { background: var(--analyse); }
  .slide-pager .plan { background: var(--plan); }
  .slide-pager .deploy { background: var(--deploy); }

  .intro-title {
    position: absolute; left: 0; top: 610px; width: 100%; text-align: center;
    font-size: 36px; font-weight: 400; color: var(--ink); letter-spacing: -1.2px;
  }
  .intro-title strong {
    display: inline-block; background: var(--brand); color: #fff; font-weight: 700;
    padding: 2px 9px 4px; margin: 0 4px;
  }
  .intro-text {
    position: absolute; left: 0; top: 679px; width: 100%; text-align: center;
    font-size: 20.5px; line-height: 30px; color: var(--muted); font-weight: 400; letter-spacing: -.3px;
  }
  .process { position: absolute; left: 0; top: 0; }
  .step-label { font-family: "Shadows Into Light", cursive; fill: var(--brand); }
</style>
</head>
<body>
<div class="site">
  <div class="topbar">
    <div class="social">
      <div class="social-dot"></div><div class="social-dot"></div><div class="social-dot"></div>
    </div>
    <div class="tools">
      <div class="tool-dot pause"><span></span><span></span></div>
      <div class="tool-dot flag"><span></span></div>
    </div>
    <div class="account"><span>Register</span><span>Login</span></div>
    <div class="search">Search...
      <svg width="12" height="12" viewBox="0 0 12 12"><circle cx="5" cy="5" r="3.8" fill="none" stroke="#bbb" stroke-width="1.6"/><line x1="8" y1="8" x2="11" y2="11" stroke="#bbb" stroke-width="1.8"/></svg>
    </div>
  </div>

  <div class="header">
    <div class="brand"><div class="brand-mark"></div><div class="brand-name">LUMERTIX</div></div>
    <nav class="nav">
      <a class="active" style="left:0">Home</a>
      <a style="left:60px">About Us</a>
      <a style="left:141px">Shop<span class="caret">&#8964;</span></a>
      <a style="left:208px">Services<span class="caret">&#8964;</span></a>
      <a style="left:294px">Portfolio</a>
      <a style="left:383px">Blog</a>
      <a style="left:440px">Careers</a>
      <a style="left:513px">Contact Us</a>
    </nav>
  </div>

  <div class="slider">
    <div class="slider-photo" role="img" aria-label="Assess banner photo: a consultant gathering information on a glass board, in orange tones"></div>
    <div class="slide-step">Step 1</div>
    <div class="slide-title">Assess</div>
    <p class="slide-text">We gather information and data to identify and delineate your central and most pressing business and IT issues.</p>
    <div class="slide-btn">Read more</div>
    <div class="slide-pager"><span class="assess"></span><span class="analyse"></span><span class="plan"></span><span class="deploy"></span></div>
  </div>

  <h1 class="intro-title">Vantor is <strong>extremely</strong> beautiful and fully responsive.</h1>
  <p class="intro-text">Lorem ipsum dolor sit amet, consectetur adipiscing elit. Fusce elementum, nulla vel pellentesque consequat, ante<br>nulla hendrerit arcu, ac tincidunt mauris lacus sed leo. vamus suscipit molestie vestibulum.</p>

  <svg class="process" width="1082" height="1178" viewBox="36 26 1082 1178">
    <path d="M36 922 C90 950 130 965 160 978" fill="none" stroke="var(--dash)" stroke-width="1.2" stroke-dasharray="10 7"/>
    <path d="M290 1020 L340 1024" fill="none" stroke="var(--dash)" stroke-width="1.2" stroke-dasharray="10 7"/>
    <path d="M470 1003 L510 994" fill="none" stroke="var(--dash)" stroke-width="1.2" stroke-dasharray="10 7"/>
    <path d="M642 950 C690 943 720 941 745 943" fill="none" stroke="var(--dash)" stroke-width="1.2" stroke-dasharray="10 7"/>
    <path d="M1045 1035 C1070 1048 1090 1060 1118 1075" fill="none" stroke="var(--dash)" stroke-width="1.2" stroke-dasharray="10 7"/>

    <rect x="160" y="845" width="44" height="44" rx="22" fill="#d4d4d4" role="img" aria-label="Small sun illustration"/>
    <rect x="652" y="845" width="101" height="48" rx="20" fill="#e6e6e6" role="img" aria-label="Small cloud illustration"/>

    <g fill="var(--circle-fill)" stroke="var(--dash)" stroke-width="1.2">
      <circle cx="226" cy="1002" r="72" fill="#fff" stroke-dasharray="5 4"/>
      <circle cx="226" cy="1002" r="66" stroke="none"/>
      <circle cx="402" cy="1002" r="72" fill="#fff" stroke-dasharray="5 4"/>
      <circle cx="402" cy="1002" r="66" stroke="none"/>
      <circle cx="578" cy="1002" r="72" fill="#fff" stroke-dasharray="5 4"/>
      <circle cx="578" cy="1002" r="66" stroke="none"/>
      <circle cx="898" cy="980" r="158" fill="#fff" stroke-dasharray="5 4"/>
      <circle cx="898" cy="980" r="152" stroke="none"/>
    </g>
    <g fill="#555" opacity=".45">
      <ellipse cx="226" cy="1083" rx="34" ry="2.5"/>
      <ellipse cx="402" cy="1083" rx="34" ry="2.5"/>
      <ellipse cx="578" cy="1083" rx="34" ry="2.5"/>
      <ellipse cx="898" cy="1156" rx="55" ry="3"/>
    </g>
    <text class="step-label" x="226" y="1120" font-size="30" text-anchor="middle">Strategy</text>
    <text class="step-label" x="402" y="1120" font-size="30" text-anchor="middle">Planning</text>
    <text class="step-label" x="578" y="1118" font-size="30" text-anchor="middle">Build</text>
    <text class="step-label" x="898" y="1194" font-size="32" text-anchor="middle">Our Work</text>
  </svg>
</div>
</body>
</html>
```